We need a new design for our construction website

We need a new website for our wordpress site ferncrestworks.co.nz

It needs to be only a few pages but sleek in design and responsive, beautifully showcasing our images and video. Currently we have
1. home
2. about us
3. contact
We need either a front page that is designed much better to showcase more content, or potentially a projects page which has images from our builds. We don't have a lot of content so the content we do have needs to be maximised by image, rather than project.

Target Market(s)

High end residential construction and renovation projects, people wanting to build a nice home, clients based in Mount Maunganui, Tauranga.

Coding

Font styles to use
Sans Serif

Colors

Designer to choose only greyscale colors for use in the design.

Requirements
Must have
• A sleek design, architectural

```html
<!DOCTYPE html>
<html lang="en">
<head>
<meta charset="utf-8">
<title>Ferncrest – About Us</title>
<link href="https://fonts.googleapis.com/css2?family=Audiowide&family=Poppins:wght@300;400;500;600&display=swap" rel="stylesheet">
<style>
:root{
  --slate:#5e6166;
  --slate-dark:#46484d;
  --slate-light:#76797e;
  --ink:#2f3033;
  --text:#6c6e72;
  --muted:#9c9ea2;
  --accent:#8c8f94;
  --accent-dark:#6f7237;
  --accent-light:#c8cacd;
  --accent-pale:#e1e2e4;
  --white:#ffffff;
  --head-font:"Audiowide",sans-serif;
  --body-font:"Poppins",sans-serif;
}
*{box-sizing:border-box;margin:0;padding:0}
html,body{width:1200px;height:4724px;overflow:hidden;background:var(--white)}
body{font-family:var(--body-font);color:var(--text);position:relative}
.photo{position:absolute}
.bar-title{position:absolute;background:linear-gradient(180deg,var(--slate-light),var(--slate-dark));color:var(--white);font-family:var(--head-font);font-weight:400;display:flex;align-items:center;justify-content:center;border-radius:6px;letter-spacing:1px}
p{font-size:11.5px;line-height:23px}

/* header */
.site-header{position:absolute;left:0;top:0;width:1200px;height:87px;background:var(--slate)}
.brand{position:absolute;left:0;top:0;width:340px;height:87px;background:var(--white);clip-path:polygon(0 0,100% 0,88% 100%,0 100%);display:flex;align-items:center;padding-left:44px;gap:14px}
.brand-stripe{position:absolute;left:300px;top:0;width:70px;height:87px;background:var(--accent-light);clip-path:polygon(55% 0,100% 0,45% 100%,0 100%)}
.brand-mark{width:40px;height:40px;border:2px solid var(--slate);border-radius:4px}
.brand-name{font-size:24px;letter-spacing:9px;color:var(--slate);font-weight:400}
.top-contacts{position:absolute;top:24px;left:418px;display:flex;gap:44px;font-size:11px;color:var(--white)}
.top-contacts span{display:flex;align-items:center;gap:8px}
.main-nav{position:absolute;top:47px;left:490px;display:flex;font-size:13px;color:var(--white)}
.main-nav a{color:var(--white);text-decoration:none;width:168px}
.main-nav a.current{color:var(--accent-light)}
.top-social{position:absolute;top:20px;right:46px;display:flex;gap:6px}
.top-social i{width:20px;height:20px;border-radius:50%;background:var(--accent);display:block}

/* hero */
.hero{position:absolute;left:0;top:87px;width:1200px;height:449px;background:linear-gradient(90deg,#e4e5e7 0%,#f4f4f4 45%,#eeeff0 75%,#cfd1d4 100%)}
.hero-box{position:absolute;left:250px;top:115px;width:700px;height:260px;background:rgba(70,72,76,.8);text-align:center;color:var(--white);padding-top:70px}
.hero-box h1{font-family:var(--head-font);font-weight:400;font-size:38px;letter-spacing:1px}
.hero-box p{font-size:13px;line-height:21px;margin:14px 70px 0}

/* who we are */
.label{position:absolute;left:64px;top:660px;font-size:14px;font-weight:600;color:var(--slate-dark);letter-spacing:1px}
.who-title{left:64px;top:705px;width:443px;height:62px;font-size:30px}
.who-text{position:absolute;left:64px;top:785px;width:445px}
.who-text p{margin-bottom:23px;font-size:11px;line-height:22.5px}
.who-side{position:absolute;left:570px;top:1020px;width:555px}
.who-side p{font-size:11px;line-height:22.5px;margin-bottom:21px}
.play{position:absolute;left:802px;top:805px;width:86px;height:86px;border:3px solid rgba(255,255,255,.85);border-radius:50%}

.mv{position:absolute;top:1308px;width:508px}
.mv h3{position:relative;height:34px;font-size:17px}
.mv p{font-size:11px;line-height:22.5px;margin-top:14px;padding-left:4px}

/* founder */
.founder-section{position:absolute;left:0;top:1503px;width:1200px;height:650px;background:linear-gradient(180deg,#f6f6f7,#e3e4e6)}
.founder-name{position:absolute;left:64px;top:1962px;width:536px;height:73px;background:rgba(58,59,62,.85);color:var(--white);text-align:center}
.founder-name h4{font-family:var(--head-font);font-weight:400;font-size:26px;margin-top:6px}
.founder-name span{font-size:11px}
.founder-social{position:absolute;left:268px;top:2057px;display:flex;gap:14px}
.founder-social i{width:22px;height:22px;border-radius:50%;background:var(--slate-light);display:block}
.years-box{left:628px;top:1600px;width:492px;height:127px;font-size:33px;line-height:62px;text-align:center;flex-direction:column}
.founder-text{position:absolute;left:628px;top:1745px;width:490px}
.founder-text p{font-size:12px;line-height:25px;letter-spacing:.6px;margin-bottom:24px}

/* contact band */
.contact-band{position:absolute;left:0;top:2153px;width:1200px;height:285px;background:linear-gradient(180deg,var(--accent),var(--accent-pale))}
.contact-title{position:absolute;left:400px;top:2180px;width:385px;text-align:center;font-family:var(--head-font);font-weight:400;font-size:37px;line-height:48px;color:var(--white)}
.field{position:absolute;background:var(--white);border:1px solid #d9dadc;font-size:11px;color:var(--muted);padding:8px 12px}
.btn-dark{position:absolute;background:var(--slate);color:var(--white);font-size:11px;display:flex;align-items:center;justify-content:center;gap:8px;border-radius:3px}

/* why best */
.why-section{position:absolute;left:0;top:2438px;width:1200px;height:768px;background:linear-gradient(180deg,#6e7074,#5d5f63 60%,#696b6f)}
.why-frame{position:absolute;left:72px;top:2510px;width:528px;height:370px;border-radius:26px;border:6px solid #1f2022;overflow:hidden}
.why-title{left:680px;top:2530px;width:435px;height:65px;font-size:30px}
.why-text{position:absolute;left:675px;top:2605px;width:420px;color:var(--white)}
.why-text p{font-size:13.5px;line-height:21px}
.badge{position:absolute;top:2888px;width:133px;height:133px;background:var(--white)}
.badge i{position:absolute;left:36px;top:36px;width:61px;height:61px;border-radius:50%;background:#c9cacd}
.badge-caption{position:absolute;top:3035px;width:340px;color:var(--white);text-align:center}
.badge-caption p{font-size:11.5px;line-height:23px}
.learn-btn{position:absolute;left:950px;top:3150px;width:167px;height:40px;background:var(--accent-light);color:var(--slate-dark);font-size:11px;display:flex;align-items:center;justify-content:center;gap:6px;border-radius:4px}

/* team */
.team-title{left:64px;top:3274px;width:1071px;height:64px;font-size:32px}
.member{position:absolute;top:3356px;width:268px;height:411px;color:var(--white);text-align:center}
.member h4{position:absolute;left:0;width:100%;top:234px;font-family:var(--head-font);font-weight:400;font-size:22px;line-height:22px}
.member .role{position:absolute;left:0;width:100%;top:290px;font-size:11px}
.member .soc{position:absolute;left:0;width:100%;top:340px;display:flex;justify-content:center;gap:22px}
.member .soc i{width:35px;height:35px;border-radius:50%;background:var(--accent-light);display:block}

/* testimony */
.testimony-title{left:64px;top:3904px;width:1071px;height:64px;font-size:32px}
.quote{position:absolute;top:4000px;width:330px;height:222px;text-align:center;padding:30px 36px 0}
.quote p{font-size:12px;line-height:25px}
.quote.featured{background:linear-gradient(180deg,var(--accent-light),var(--accent));color:var(--white)}
.author{display:flex;align-items:center;justify-content:center;gap:12px;margin-top:16px;text-align:left}
.author .ava{width:56px;height:56px;border-radius:50%;background:linear-gradient(135deg,#c4c5c7,#6e7073)}
.author b{display:block;font-weight:400;font-size:15px;color:var(--ink)}
.author small{font-size:10px;color:var(--muted)}
.featured .author b,.featured .author small{color:var(--white)}

/* footer */
.site-footer{position:absolute;left:0;top:4340px;width:1200px;height:384px;background:var(--slate);clip-path:polygon(0 140px,50% 0,100% 140px,100% 100%,0 100%)}
.footer-brand{position:absolute;left:468px;top:4438px;display:flex;align-items:center;gap:14px}
.footer-brand .brand-mark{border-color:var(--white)}
.footer-brand .brand-name{color:var(--white)}
.footer-nav{position:absolute;left:436px;top:4512px;display:flex;gap:34px;font-size:13px;color:var(--white)}
.footer-nav .current{color:var(--accent-light)}
.footer-contacts{position:absolute;left:380px;top:4566px;display:flex;gap:34px;font-size:11px;color:var(--white)}
.footer-contacts span{display:flex;align-items:center;gap:8px}
.footer-contacts svg{color:var(--accent-light)}
.footer-social{position:absolute;left:530px;top:4603px;display:flex;gap:12px}
.footer-social i{width:26px;height:26px;border-radius:50%;background:var(--accent-light);display:block}
.copyright{position:absolute;left:0;width:1200px;top:4684px;text-align:center;font-size:13px;color:var(--white)}
</style>
</head>
<body>

<svg width="0" height="0" style="position:absolute">
  <defs>
    <symbol id="i-mail" viewBox="0 0 16 12"><rect x="0.5" y="0.5" width="15" height="11" rx="1" fill="none" stroke="currentColor"/><path d="M1 1l7 6 7-6" fill="none" stroke="currentColor"/></symbol>
    <symbol id="i-phone" viewBox="0 0 16 16"><path d="M3 1l3 3-2 2c1 2 4 5 6 6l2-2 3 3-2 2C7 15 1 9 1 3z" fill="currentColor"/></symbol>
  </defs>
</svg>

<header class="site-header">
  <div class="brand-stripe"></div>
  <div class="brand"><span class="brand-mark"></span><span class="brand-name">FERNCREST</span></div>
  <div class="top-contacts">
    <span><svg width="14" height="11"><use href="#i-mail"/></svg>liam@ferncrestworks.co.nz</span>
    <span><svg width="14" height="11"><use href="#i-mail"/></svg>admin@ferncrestworks.co.nz</span>
    <span><svg width="12" height="12"><use href="#i-phone"/></svg>027 481 3390</span>
  </div>
  <nav class="main-nav"><a>HOME</a><a class="current">ABOUT</a><a>SERVICES</a><a>CONTACT</a></nav>
  <div class="top-social"><i></i><i></i><i></i><i></i><i></i></div>
</header>

<section class="hero" role="img" aria-label="Apartment building with a smiling builder in a hard hat">
  <div class="hero-box">
    <h1>ABOUT US</h1>
    <p>Lorem ipsum dolor sit amet, consectetur adipiscing elit. Ut elit tellus, luctus nec ullamcorper mattis, pulvinar dapibus leo.Ut elit tellus, luctus nec ullamcorper mattis, pulvinar dapibus leo.</p>
  </div>
</section>

<div class="label">ABOUT US</div>
<h2 class="bar-title who-title">WHO WE ARE?</h2>
<div class="who-text">
  <p>Kauri Ridge Homes Ltd T/A <b>Ferncrest</b> was founded in 1985 by Grant Whitfield and began trading as Ferncrest in 2017 with sons Liam and Owen at the helm. With the company's roots previously in solid timber, the team have a special interest in architectural homes, alternative building technologies and sustainable building practices. Ferncrest's team have an exceptional understanding of alternative building materials and are happy to work with your architect or designer to ensure your build is as enjoyable and hassle-free as possible.</p>
  <p>Liam has more than 15 years building experience and is our Managing Director, he is described by our customers as a problem solver, personable, down to earth and passionate about quality and the building performance of homes. Owen is Ferncrest's Site Manager and has a passion for technical construction and alternative building technologies. Together Liam &amp; Owen provide clients with a strong foundation of knowledge, skill and care, providing attention to detail across the entire project and its management.</p>
</div>
<div class="photo" style="left:570px;top:693px;width:555px;height:312px;background:linear-gradient(160deg,#c4c6c9,#96989c 45%,#a9abae 75%,#cdcfd1)" role="img" aria-label="Three builders in hard hats reviewing plans in front of a tower crane"></div>
<div class="play"></div>
<div class="who-side">
  <p>Liam, Owen and our team of carpenters enjoy working closely with our customers, respecting your right to always have a clear understanding of where things are at with your building project.</p>
  <p>Our vision is to build beautiful, efficient homes with the best building technologies available that our customers are proud to own.</p>
</div>

<div class="mv" style="left:78px">
  <h3 class="bar-title">OUR MISSION</h3>
  <p>Faucibus in ornare quam viverra orci. Sapien pellentesque habitant morbi tristique senectus et netus. Nulla aliquet enim tortor at. Nulla aliquet enim tortor at.</p>
</div>
<div class="mv" style="left:614px">
  <h3 class="bar-title">OUR VISION</h3>
  <p>Faucibus in ornare quam viverra orci. Sapien pellentesque habitant morbi tristique senectus et netus. Nulla aliquet enim tortor at. Nulla aliquet enim tortor at.</p>
</div>

<section class="founder-section"></section>
<div class="photo" style="left:64px;top:1630px;width:536px;height:453px;background:linear-gradient(180deg,#eceded,#d8d9db 55%,#a4a6a9 80%,#e6e7e8)" role="img" aria-label="Portrait of the company founder in a hard hat and safety vest"></div>
<div class="founder-name"><h4>GRANT WHITFIELD</h4><span>CEO FERNCREST</span></div>
<div class="founder-social"><i></i><i></i><i></i><i></i></div>
<div class="bar-title years-box"><span>35 YEARS AS</span><span>ARCHITECTURE</span></div>
<div class="founder-text">
  <p>Lorem ipsum dolor sit amet, consectetuer adipiscing elit. Phasellus ullamcorper ipsum rutrum nunc.</p>
  <p>Aliquet elit ac nisl vestibulum odio. Quisque id mi nullam cursus lacinia erat. Ut a nisl id ante tempus hendrerit.</p>
  <p>Morbi nec metus. Nunc nonummy metus. Praesent porttitor, nulla vitae posuere iaculis, arcu nisl dignissim dolor, a pretium mi sem ut ipsum.</p>
  <p>Lorem ipsum dolor sit amet, consectetuer adipiscing elit. Phasellus ullamcorper ipsum rutrum nunc.</p>
</div>

<section class="contact-band"></section>
<div class="photo" style="left:105px;top:2105px;width:125px;height:280px;background:linear-gradient(180deg,#3a3b3e,#222326)" role="img" aria-label="Businesswoman in a dark suit holding a folder"></div>
<div class="btn-dark" style="left:64px;top:2385px;width:214px;height:44px"><svg width="10" height="10"><use href="#i-phone"/></svg>CALL US 027 481 3390</div>
<h2 class="contact-title">GET IN TOUCH</h2>
<div class="field" style="left:400px;top:2250px;width:120px;height:34px">Name</div>
<div class="field" style="left:526px;top:2250px;width:118px;height:34px">Email</div>
<div class="field" style="left:650px;top:2250px;width:120px;height:34px">Phone</div>
<div class="field" style="left:400px;top:2294px;width:370px;height:84px">Message</div>
<div class="btn-dark" style="left:400px;top:2388px;width:370px;height:40px">SEND MESSAGE</div>
<div class="photo" style="left:915px;top:2100px;width:190px;height:275px;background:linear-gradient(180deg,#f2f2f3,#8a8c90 60%,#55575b)" role="img" aria-label="Smiling builder in a white hard hat carrying a spirit level"></div>
<div class="btn-dark" style="left:905px;top:2376px;width:215px;height:40px">CONTACT US</div>

<section class="why-section"></section>
<div class="why-frame"><div class="photo" style="inset:0;background:linear-gradient(100deg,#d9dadc,#aeb0b3 45%,#e6e6e7 70%,#8c8e91)" role="img" aria-label="Engineer in a white hard hat studying architectural plans with city towers behind"></div></div>
<h2 class="bar-title why-title">WHY WE ARE BEST?</h2>
<div class="why-text"><p>Laboris optio est commodo aliqua ante purus beatae reprehenderit, temporibus dolore atione anr condimentum conubia unde nam pretium netus numquam odit repellat! Justo quidem, quidem ac illum ration ulis lorem primis accusamus laboris sam sint incididunt venen. Faucibus in ornare quam viverra orci. Sapien pellentesque habitant morbi tristique senectus et netus. Nulla aliquet enim tortor at. Nulla aliquet enim tortor at.</p></div>
<div class="badge" style="left:182px"><i></i></div>
<div class="badge" style="left:533px"><i style="background:#2b2c2e"></i></div>
<div class="badge" style="left:883px"><i style="background:#8f9194"></i></div>
<div class="badge-caption" style="left:80px"><p>Faucibus in ornare quam viverra orci. Sapien pellentesque habitant morbi tristique senectus et netus. Nulla aliquet enim tortor at. Nulla aliquet enim tortor at.</p></div>
<div class="badge-caption" style="left:430px"><p>Faucibus in ornare quam viverra orci. Sapien pellentesque habitant morbi tristique senectus et netus. Nulla aliquet enim tortor at. Nulla aliquet enim tortor at.</p></div>
<div class="badge-caption" style="left:780px"><p>Faucibus in ornare quam viverra orci. Sapien pellentesque habitant morbi tristique senectus et netus. Nulla aliquet enim tortor at. Nulla aliquet enim tortor at.</p></div>
<div class="learn-btn">LEARN MORE <svg width="10" height="10" viewBox="0 0 10 10"><circle cx="5" cy="5" r="5" fill="#46484d"/><path d="M4 3l2 2-2 2" stroke="#c8cacd" fill="none" stroke-width="1.4"/></svg></div>

<h2 class="bar-title team-title">OUR TEAM</h2>
<div class="member" style="left:64px">
  <div class="photo" style="inset:0;background:linear-gradient(180deg,#cbcccf,#6f7074 60%,#5a5c60)" role="img" aria-label="Team member in a checked shirt holding a hard hat"></div>
  <h4>AARON<br>PETLEY</h4><div class="role">CEO FERNCREST</div><div class="soc"><i></i><i></i><i></i></div>
</div>
<div class="member" style="left:332px">
  <div class="photo" style="inset:0;background:linear-gradient(180deg,#efefef,#a9abae 60%,#808286)" role="img" aria-label="Team member in a striped shirt, smiling"></div>
  <h4>MIA HOLLIS</h4><div class="role">MANAGER</div><div class="soc"><i></i><i></i><i></i></div>
</div>
<div class="member" style="left:600px">
  <div class="photo" style="inset:0;background:linear-gradient(180deg,#d8d9da,#7e7f82 60%,#4a4c50)" role="img" aria-label="Bearded team member with glasses in a grey jacket"></div>
  <h4>DANIEL<br>FROST</h4><div class="role">TEAM LEADER</div><div class="soc"><i></i><i></i><i></i></div>
</div>
<div class="member" style="left:867px">
  <div class="photo" style="inset:0;background:linear-gradient(180deg,#e2e3e5,#505256 60%,#404145)" role="img" aria-label="Team member in a dark suit and tie"></div>
  <h4>RUBEN<br>CARROW</h4><div class="role">CIVIL ENGINEER</div><div class="soc"><i></i><i></i><i></i></div>
</div>

<h2 class="bar-title testimony-title">TESTIMONY</h2>
<div class="quote" style="left:82px">
  <p>Click edit button to change this text. Lorem ipsum dolor sit amet, consectetur adipiscing elit. Ut elit tellus, luctus nec ullamcorper mattis, pulvinar dapibus leo.</p>
  <div class="author"><span class="ava" role="img" aria-label="Client portrait"></span><div><b>Tessa Lowe</b><small>DESIGNER</small></div></div>
</div>
<div class="quote featured" style="left:436px">
  <p>Click edit button to change this text. Lorem ipsum dolor sit amet, consectetur adipiscing elit. Ut elit tellus, luctus nec ullamcorper mattis, pulvinar dapibus leo.</p>
  <div class="author"><span class="ava" role="img" aria-label="Client portrait"></span><div><b>Nina Ashford</b><small>DESIGNER</small></div></div>
</div>
<div class="quote" style="left:790px">
  <p>Click edit button to change this text. Lorem ipsum dolor sit amet, consectetur adipiscing elit. Ut elit tellus, luctus nec ullamcorper mattis, pulvinar dapibus leo.</p>
  <div class="author"><span class="ava" role="img" aria-label="Client portrait"></span><div><b>Sam Keller</b><small>DESIGNER</small></div></div>
</div>

<footer class="site-footer"></footer>
<div class="footer-brand"><span class="brand-mark"></span><span class="brand-name">FERNCREST</span></div>
<nav class="footer-nav"><span>HOME</span><span class="current">ABOUT</span><span>SERVICES</span><span>CONTACT</span></nav>
<div class="footer-contacts">
  <span><svg width="14" height="11"><use href="#i-mail"/></svg>liam@ferncrestworks.co.nz</span>
  <span><svg width="14" height="11"><use href="#i-mail"/></svg>admin@ferncrestworks.co.nz</span>
  <span><svg width="12" height="12"><use href="#i-phone"/></svg>027 481 3390</span>
</div>
<div class="footer-social"><i></i><i></i><i></i><i></i></div>
<div class="copyright">Copyright © 2020 Ferncrest Works</div>

</body>
</html>
```